A book main title will be, "Kindle Your Clients"
The subtext will be, "Win the market with a story that sparks"
Would like it to blend with my web site brand. You can find it here: www.kindleyourclients-demo.net

Audience is business and revenue leaders for small, medium and large businesses. They have a new solution, or want to enter a new market, and they need to "inspire their buyers" meaning getting the buyers to want to change enough to overcome their status quo bias. They need a story that sizzles to do this.

```html
<!DOCTYPE html>
<html lang="en">
<head>
<meta charset="utf-8">
<title>Kindle Your Clients – Book Cover</title>
<link rel="stylesheet" href="https://fonts.googleapis.com/css2?family=Lato:wght@300;400;700;900&display=swap">
<style>
  :root {
    --page-bg: #ffffff;
    --cover-bg: #d9e6ef;
    --cover-fog: #e4edf3;
    --shirt-blue: #7592b8;
    --shirt-mid: #a7bcd2;
    --title-pink: #e8677a;
    --title-teal: #4fc0b5;
    --ink: #1d1d1f;
    --ink-soft: #2a2a2c;
    --mark-tint: #f1f5f7;
  }
  * { margin: 0; padding: 0; box-sizing: border-box; }
  html, body {
    width: 1200px; height: 1200px; overflow: hidden;
    background: var(--page-bg);
    font-family: "Lato", Arial, sans-serif;
  }
  .canvas { position: relative; width: 1200px; height: 1200px; }
  .cover {
    position: absolute; left: 321px; top: 181px;
    width: 558px; height: 837px;
    background: var(--cover-bg);
    overflow: hidden;
    text-align: center;
  }
  .cover-photo {
    position: absolute; left: 0; top: 0; width: 100%; height: 360px;
    background:
      linear-gradient(90deg, rgba(220,231,240,0.85) 0%, rgba(220,231,240,0) 45%),
      linear-gradient(180deg, var(--shirt-blue) 0%, var(--shirt-mid) 58%, var(--cover-fog) 62%, var(--cover-bg) 100%);
  }
  .cover-photo::after {
    content: ""; position: absolute; left: 0; right: 0; bottom: 0; height: 150px;
    background: linear-gradient(180deg, rgba(217,230,239,0) 0%, var(--cover-fog) 60%, var(--cover-bg) 100%);
  }
  .title-line { position: absolute; left: 0; right: 0; line-height: 1; display: block; }
  .title-kindle { top: 280px; color: var(--title-pink); font-weight: 900; font-size: 105px; }
  .title-your { top: 382px; color: var(--ink); font-weight: 300; font-size: 80px; }
  .title-clients { top: 460px; color: var(--title-teal); font-weight: 900; font-size: 90px; }
  .subtitle {
    position: absolute; left: 0; right: 0; top: 567px;
    font-size: 21px; font-weight: 400; color: var(--ink-soft); line-height: 27px;
    text-transform: uppercase;
  }
  .publisher {
    position: absolute; left: 0; right: 0; top: 688px;
    display: flex; justify-content: center; align-items: center; gap: 8px;
    color: var(--mark-tint); font-size: 15px; font-weight: 700; letter-spacing: 1px;
  }
  .publisher-dot { width: 12px; height: 12px; border-radius: 50%; background: var(--mark-tint); }
  .author {
    position: absolute; left: 0; right: 0; top: 752px; line-height: 26px;
    font-size: 21px; font-weight: 700; color: var(--ink-soft); text-transform: uppercase;
  }
  .website {
    position: absolute; left: 0; right: 0; top: 781px; line-height: 24px;
    font-size: 19px; font-weight: 700; color: var(--ink-soft);
  }
</style>
</head>
<body>
  <main class="canvas">
    <section class="cover">
      <div class="cover-photo" role="img" aria-label="Photo of a hand holding a red horseshoe magnet above small metal figures of people on a glossy table"></div>
      <h1 class="title">
        <span class="title-line title-kindle">KINDLE</span>
        <span class="title-line title-your">YOUR</span>
        <span class="title-line title-clients">CLIENTS</span>
      </h1>
      <p class="subtitle">Win the market with a story<br>that sparks</p>
      <div class="publisher"><span class="publisher-dot"></span><span>EMBER STORY CO.</span></div>
      <p class="author">Dale Morrow, The Story Fixer</p>
      <p class="website">www.kindleyourclients-demo.net</p>
    </section>
  </main>
</body>
</html>
```